75%-100% OFF - Insulation Banner Design

Need banners created for an online marketing push for my insulation business V7K Energy.

www.v7kenergy.example

Specifically - I would like the banners to pop utilizing our colors in neon. To see samples of colors we use - visit our asset folder.

https://files.storvault.example/folders/9xQmT42pLkWe7HnZbRcY3uVa0dJfGsNo?share=link

I will attach sample files to this project.

The banner must highlight 75%-100% off Insulation and Weatherization. If you can include our current perfect Yorbel reviews somewhere in the advertisement that would be awesome but not a requirement.

The banner must meet Tilwick Renew logo guidelines. Please see attachment.

Target Market(s)

Home Owners

Industry/Entity Type

Insulation and Construction

Font styles to use
Sans Serif

Colors
59FF00
82FF00
B8FF75
E3FFCB
F4FFEA

Requirements
Must have
• Tilwick Renew Logo per project description. Must have 75-100% off somewhere that is very clear. And must have our company V7K Energy Logo.
Nice to have
• V7K Energy Logo

```html
<!DOCTYPE html>
<html lang="en">
<head>
<meta charset="utf-8">
<title>V7K Energy – Insulation Banner Set</title>
<link href="https://fonts.googleapis.com/css2?family=Oswald:wght@500;700&family=Poppins:wght@500;600;700&display=swap" rel="stylesheet">
<style>
  :root{
    --stage:#cbcbcb;
    --paper:#ffffff;
    --navy:#1b4f7c;
    --neon:#5cff00;
    --red:#e1251b;
    --ink:#141414;
    --grey:#555555;
    --star:#f5b400;
    --leaf:#3c8a1e;
    --photo-dark:#23361c;
    --photo-mid:#5d6b2e;
    --photo-glow:#ffd27a;
  }
  *{box-sizing:border-box;margin:0;padding:0}
  html,body{width:1200px;height:1200px;overflow:hidden;background:var(--stage)}
  body{position:relative;font-family:"Poppins",Arial,sans-serif}
  .banner{position:absolute;background:var(--paper);overflow:hidden;box-shadow:0 4px 14px rgba(0,0,0,.28)}
  .abs{position:absolute}
  .logo-row{position:absolute;display:flex;align-items:center;white-space:nowrap}
  .brand{font-family:"Poppins",Arial,sans-serif;font-weight:600;color:var(--navy);display:flex;align-items:center;white-space:nowrap;line-height:1}
  .brand-mark{display:inline-block;background:var(--navy);flex:none}
  .partner{font-family:"Poppins",Arial,sans-serif;font-weight:700;color:var(--leaf);white-space:nowrap;line-height:1}
  .headline{font-family:"Oswald",Arial,sans-serif;font-weight:700;line-height:1;white-space:nowrap}
  .headline .pct{color:var(--navy)}
  .headline .off{color:var(--red)}
  .band{background:var(--neon);font-family:"Oswald",Arial,sans-serif;font-weight:700;color:var(--ink);text-transform:uppercase;line-height:1.05}
  .phone-pill{display:flex;align-items:center;background:var(--navy);color:#fff;font-family:"Oswald",Arial,sans-serif;font-weight:700;border-radius:5px;white-space:nowrap;padding-right:8px}
  .phone-pill .dot{background:#fff;border-radius:50%;display:flex;align-items:center;justify-content:center;border:2px solid var(--navy);flex:none}
  .click-btn{display:flex;align-items:center;justify-content:center;gap:4px;background:var(--navy);color:#fff;font-family:"Oswald",Arial,sans-serif;font-weight:500;border-radius:5px;white-space:nowrap}
  .reviews{font-family:"Poppins",Arial,sans-serif;line-height:1.05;white-space:nowrap}
  .reviews .name{font-weight:600;color:var(--navy);display:block}
  .reviews .label{color:var(--grey);font-weight:500}
  .reviews .stars{color:var(--star)}
  .site{display:flex;align-items:center;gap:6px;font-weight:700;color:var(--navy);white-space:nowrap}
  .photo{position:absolute;border-radius:50%;border:6px solid var(--navy);
    background:radial-gradient(circle at 50% 42%,var(--photo-glow) 0%,#e79b3a 14%,var(--photo-mid) 36%,var(--photo-dark) 72%)}
</style>
</head>
<body>

<!-- Skyscraper 200 x 750 -->
<section class="banner" style="left:307px;top:69px;width:200px;height:750px">
  <div class="brand abs" style="left:0;width:200px;justify-content:center;gap:5px;top:26px;font-size:24px"><span class="brand-mark" style="width:14px;height:14px"></span>V7K Energy</div>
  <div class="partner abs" style="left:0;width:200px;text-align:center;top:82px;font-size:18px">Tilwick Renew</div>
  <div class="headline abs" style="left:0;width:200px;text-align:center;top:140px;font-size:38px"><span class="pct">75%-100%</span><br><span class="off">OFF</span></div>
  <div class="band abs" style="left:0;top:231px;width:200px;height:112px;font-size:22px;display:flex;align-items:center;justify-content:center;text-align:center">Insulation<br>and<br>Weatherization</div>
  <div class="phone-pill abs" style="left:12px;top:381px;height:28px;font-size:22px">
    <span class="dot" style="width:28px;height:28px;margin-right:4px"><svg width="14" height="14" viewBox="0 0 24 24"><path fill="#3c8a1e" d="M6.6 10.8c1.4 2.8 3.8 5.1 6.6 6.6l2.2-2.2c.3-.3.7-.4 1-.2 1.1.4 2.3.6 3.6.6.6 0 1 .4 1 1V20c0 .6-.4 1-1 1C10.6 21 3 13.4 3 4c0-.6.4-1 1-1h3.5c.6 0 1 .4 1 1 0 1.3.2 2.5.6 3.6.1.3 0 .7-.2 1z"/></svg></span>555-214-3076
  </div>
  <div class="reviews abs" style="left:40px;top:418px;font-size:10px"><span class="name" style="font-size:22px">Yorbel</span><span class="label">REVIEWS </span><span class="stars">★★★★★</span></div>
  <div class="click-btn abs" style="left:38px;top:476px;width:124px;height:34px;font-size:17px">CLICK HERE
    <svg width="18" height="18" viewBox="0 0 24 24"><circle cx="12" cy="12" r="11" fill="#fff"/><path fill="#1b4f7c" d="M10 6h2v6h1V9h2v4h1v-2h2v6l-2 3h-5l-3-4 1-1 1 1z"/></svg>
  </div>
  <div class="photo" role="img" aria-label="Glowing light bulb planted in soil with seedlings, green bokeh background" style="left:-40px;top:537px;width:280px;height:280px"></div>
</section>

<!-- Small square 312 x 250 -->
<section class="banner" style="left:584px;top:165px;width:312px;height:250px">
  <div class="photo" role="img" aria-label="Glowing light bulb planted in soil with seedlings" style="left:170px;top:-20px;width:290px;height:290px"></div>
  <div class="logo-row" style="left:14px;top:16px;height:26px;gap:6px">
    <span class="brand" style="font-size:13px;gap:4px"><span class="brand-mark" style="width:9px;height:9px"></span>V7K Energy</span>
    <span class="partner" style="font-size:9.5px">Tilwick Renew</span>
  </div>
  <div class="headline abs" style="left:14px;top:56px;font-size:24px"><span class="pct">75%-100%</span> <span class="off">OFF</span></div>
  <div class="band abs" style="left:0;top:86px;width:170px;height:60px;font-size:18px;padding:6px 0 0 14px">Insulation and<br>Weatherization</div>
  <div class="click-btn abs" style="left:16px;top:154px;width:70px;height:22px;font-size:11px">CLICK HERE</div>
  <div class="reviews abs" style="left:92px;top:150px;font-size:7px"><span class="name" style="font-size:14px">Yorbel</span><span class="label">REVIEWS </span><span class="stars">★★★★★</span></div>
  <div class="phone-pill abs" style="left:16px;top:196px;height:24px;font-size:19px">
    <span class="dot" style="width:24px;height:24px;margin-right:3px"><svg width="12" height="12" viewBox="0 0 24 24"><path fill="#3c8a1e" d="M6.6 10.8c1.4 2.8 3.8 5.1 6.6 6.6l2.2-2.2c.3-.3.7-.4 1-.2 1.1.4 2.3.6 3.6.6.6 0 1 .4 1 1V20c0 .6-.4 1-1 1C10.6 21 3 13.4 3 4c0-.6.4-1 1-1h3.5c.6 0 1 .4 1 1 0 1.3.2 2.5.6 3.6.1.3 0 .7-.2 1z"/></svg></span>555-214-3076
  </div>
  <div class="site abs" style="left:20px;top:224px;font-size:13px"><svg width="14" height="14" viewBox="0 0 24 24"><circle cx="12" cy="12" r="10" fill="none" stroke="#3c8a1e" stroke-width="2.5"/><path d="M2 12h20M12 2c3 3 3 17 0 20M12 2c-3 3-3 17 0 20" fill="none" stroke="#3c8a1e" stroke-width="2"/></svg>www.v7kenergy.example</div>
</section>

<!-- Medium rectangle 375 x 312 -->
<section class="banner" style="left:552px;top:464px;width:375px;height:312px">
  <div class="photo" role="img" aria-label="Glowing light bulb planted in soil with seedlings" style="left:197px;top:4px;width:310px;height:310px"></div>
  <div class="logo-row" style="left:16px;top:24px;height:30px;gap:10px">
    <span class="brand" style="font-size:17px;gap:5px"><span class="brand-mark" style="width:11px;height:11px"></span>V7K Energy</span>
    <span class="partner" style="font-size:12px">Tilwick Renew</span>
  </div>
  <div class="headline abs" style="left:14px;top:82px;font-size:29px"><span class="pct">75%-100%</span> <span class="off">OFF</span></div>
  <div class="band abs" style="left:0;top:117px;width:196px;height:65px;font-size:21px;padding:6px 0 0 14px">Insulation and<br>Weatherization</div>
  <div class="click-btn abs" style="left:20px;top:198px;width:78px;height:26px;font-size:12px">CLICK HERE</div>
  <div class="reviews abs" style="left:106px;top:195px;font-size:8px"><span class="name" style="font-size:16px">Yorbel</span><span class="label">REVIEWS </span><span class="stars">★★★★★</span></div>
  <div class="phone-pill abs" style="left:18px;top:243px;height:27px;font-size:22px">
    <span class="dot" style="width:27px;height:27px;margin-right:4px"><svg width="13" height="13" viewBox="0 0 24 24"><path fill="#3c8a1e" d="M6.6 10.8c1.4 2.8 3.8 5.1 6.6 6.6l2.2-2.2c.3-.3.7-.4 1-.2 1.1.4 2.3.6 3.6.6.6 0 1 .4 1 1V20c0 .6-.4 1-1 1C10.6 21 3 13.4 3 4c0-.6.4-1 1-1h3.5c.6 0 1 .4 1 1 0 1.3.2 2.5.6 3.6.1.3 0 .7-.2 1z"/></svg></span>555-214-3076
  </div>
  <div class="site abs" style="left:22px;top:276px;font-size:15px"><svg width="16" height="16" viewBox="0 0 24 24"><circle cx="12" cy="12" r="10" fill="none" stroke="#3c8a1e" stroke-width="2.5"/><path d="M2 12h20M12 2c3 3 3 17 0 20M12 2c-3 3-3 17 0 20" fill="none" stroke="#3c8a1e" stroke-width="2"/></svg>www.v7kenergy.example</div>
</section>

<!-- Leaderboard 585 x 75 -->
<section class="banner" style="left:307px;top:887px;width:585px;height:75px">
  <div class="photo" role="img" aria-label="Glowing light bulb in soil with green bokeh" style="left:455px;top:-70px;width:220px;height:220px;border-width:4px"></div>
  <div class="band abs" style="left:146px;top:0;width:310px;height:46px;clip-path:polygon(4% 0,100% 0,100% 100%,0 100%)"></div>
  <div class="logo-row" style="left:10px;top:12px;height:22px;gap:5px">
    <span class="brand" style="font-size:10px;gap:3px"><span class="brand-mark" style="width:7px;height:7px"></span>V7K Energy</span>
    <span class="partner" style="font-size:7px">Tilwick Renew</span>
  </div>
  <div class="headline abs" style="left:160px;top:3px;font-size:22px"><span class="pct">75%-100%</span><span class="off">OFF</span></div>
  <div class="headline abs" style="left:160px;top:26px;font-size:18px;color:var(--ink)">INSULATION AND WEATHERIZATION</div>
  <div class="phone-pill abs" style="left:16px;top:51px;height:18px;font-size:14px;padding-right:5px">
    <span class="dot" style="width:18px;height:18px;margin-right:2px"><svg width="9" height="9" viewBox="0 0 24 24"><path fill="#3c8a1e" d="M6.6 10.8c1.4 2.8 3.8 5.1 6.6 6.6l2.2-2.2c.3-.3.7-.4 1-.2 1.1.4 2.3.6 3.6.6.6 0 1 .4 1 1V20c0 .6-.4 1-1 1C10.6 21 3 13.4 3 4c0-.6.4-1 1-1h3.5c.6 0 1 .4 1 1 0 1.3.2 2.5.6 3.6.1.3 0 .7-.2 1z"/></svg></span>555-214-3076
  </div>
  <div class="site abs" style="left:140px;top:53px;font-size:11px;gap:4px"><svg width="11" height="11" viewBox="0 0 24 24"><circle cx="12" cy="12" r="10" fill="none" stroke="#3c8a1e" stroke-width="2.5"/><path d="M2 12h20M12 2c3 3 3 17 0 20M12 2c-3 3-3 17 0 20" fill="none" stroke="#3c8a1e" stroke-width="2"/></svg>www.v7kenergy.example</div>
  <div class="click-btn abs" style="left:326px;top:54px;width:54px;height:15px;font-size:9px">CLICK HERE</div>
  <div class="reviews abs" style="left:392px;top:50px;font-size:5px"><span class="name" style="font-size:11px">Yorbel</span><span class="label">REVIEWS </span><span class="stars">★★★★★</span></div>
</section>

<!-- Large leaderboard 910 x 112 -->
<section class="banner" style="left:145px;top:1011px;width:910px;height:112px">
  <div class="photo" role="img" aria-label="Glowing light bulb planted in soil with seedlings" style="left:700px;top:-110px;width:340px;height:340px"></div>
  <div class="band abs" style="left:208px;top:0;width:496px;height:74px;clip-path:polygon(3% 0,100% 0,100% 100%,0 100%)"></div>
  <div class="logo-row" style="left:14px;top:20px;height:32px;gap:7px">
    <span class="brand" style="font-size:15px;gap:4px"><span class="brand-mark" style="width:10px;height:10px"></span>V7K Energy</span>
    <span class="partner" style="font-size:10px">Tilwick Renew</span>
  </div>
  <div class="headline abs" style="left:238px;top:2px;font-size:34px"><span class="pct">75%-100%</span><span class="off">OFF</span></div>
  <div class="headline abs" style="left:236px;top:40px;font-size:30px;color:var(--ink)">INSULATION AND WEATHERIZATION</div>
  <div class="phone-pill abs" style="left:14px;top:75px;height:28px;font-size:23px">
    <span class="dot" style="width:28px;height:28px;margin-right:4px"><svg width="14" height="14" viewBox="0 0 24 24"><path fill="#3c8a1e" d="M6.6 10.8c1.4 2.8 3.8 5.1 6.6 6.6l2.2-2.2c.3-.3.7-.4 1-.2 1.1.4 2.3.6 3.6.6.6 0 1 .4 1 1V20c0 .6-.4 1-1 1C10.6 21 3 13.4 3 4c0-.6.4-1 1-1h3.5c.6 0 1 .4 1 1 0 1.3.2 2.5.6 3.6.1.3 0 .7-.2 1z"/></svg></span>555-214-3076
  </div>
  <div class="site abs" style="left:206px;top:76px;font-size:19px"><svg width="20" height="20" viewBox="0 0 24 24"><circle cx="12" cy="12" r="10" fill="none" stroke="#3c8a1e" stroke-width="2.5"/><path d="M2 12h20M12 2c3 3 3 17 0 20M12 2c-3 3-3 17 0 20" fill="none" stroke="#3c8a1e" stroke-width="2"/></svg>www.v7kenergy.example</div>
  <div class="click-btn abs" style="left:494px;top:80px;width:90px;height:24px;font-size:14px">CLICK HERE</div>
  <div class="reviews abs" style="left:596px;top:75px;font-size:8px"><span class="name" style="font-size:17px">Yorbel</span><span class="label">REVIEWS </span><span class="stars">★★★★</span></div>
</section>

</body>
</html>
```